Corvelian Magazine Ad

We are looking for an ad design to use for a plastic surgery practice advertising in a glossy print add. we have a good idea of what we need, and need a designer to put together the words and pictures and add a bit of elegant flair.

Target Market(s)

high end readers looking to purchase cosmetic surgery services

Industry/Entity Type

Advertising

```html
<!DOCTYPE html>
<html lang="en">
<head>
<meta charset="utf-8">
<title>Corvelian Magazine Ad – Breast and Body Solutions</title>
<link href="https://fonts.googleapis.com/css2?family=Josefin+Sans:wght@400;600&family=Arimo:wght@400;700&family=Open+Sans:wght@400;600;700&family=Roboto+Condensed:wght@300;400;700&display=swap" rel="stylesheet">
<style>
  :root{
    --stage:#000000;
    --guide:#2bdc1f;
    --header-red:#6e0202;
    --footer-red:#b00b0b;
    --locations-red:#5e0303;
    --panel-gray:#c8c8c8;
    --white:#ffffff;
    --ink:#111111;
    --accent-red:#e30d0d;
    --accent-green:#1fa51f;
    --muted:#d9b3b3;
    --brand-blue:#2a5fc4;
  }
  *{margin:0;padding:0;box-sizing:border-box}
  html,body{width:1200px;height:1000px;overflow:hidden;background:var(--stage)}
  .stage{position:relative;width:1200px;height:1000px}

  .guide-line{position:absolute;background:var(--guide)}
  .guide-label{position:absolute;border:3px solid var(--guide);background:var(--stage);color:var(--white);
    font-family:"Open Sans",sans-serif;font-weight:700;font-size:15px;line-height:17px;text-align:center;padding-top:4px}

  .ad{position:absolute;left:348px;top:140px;width:503px;height:719px;background:var(--white);overflow:hidden}

  .header{position:absolute;left:0;top:0;width:503px;height:136px;background:var(--header-red);
    color:var(--white);font-family:"Josefin Sans",sans-serif;text-align:center}
  .header .name{position:absolute;top:33px;width:100%;font-size:29px;letter-spacing:.2px}
  .header .title{position:absolute;top:78px;width:100%;font-size:31px;font-variant:small-caps;letter-spacing:0}

  .doctor-panel{position:absolute;left:0;top:136px;width:109px;height:325px;background:var(--panel-gray)}
  .portrait{position:absolute;left:10px;top:57px;width:91px;height:110px;border:3px solid var(--accent-red);
    background:linear-gradient(90deg,#7a2a14 0%,#3a2a28 30%,#23222c 60%,#b08a50 100%)}
  .doctor-name{position:absolute;left:11px;top:172px;font-family:"Roboto Condensed",sans-serif;font-weight:700;font-size:9.5px;color:var(--ink)}
  .doctor-cred{position:absolute;left:11px;top:185px;font-family:"Roboto Condensed",sans-serif;font-weight:300;font-size:7.5px;line-height:9.5px;color:var(--ink)}
  .specialty{position:absolute;left:0;top:220px;width:109px;height:39px;background:var(--white);padding:4px 0 0 10px;
    font-family:"Roboto Condensed",sans-serif;font-weight:300;font-size:8px;line-height:10px;color:var(--ink)}

  .hero{position:absolute;left:109px;top:136px;width:217px;height:325px;
    background:radial-gradient(ellipse 40% 45% at 52% 45%,#6f7c92 0%,#3a3e48 35%,#141414 70%,#080808 100%)}

  .info-panel{position:absolute;left:326px;top:136px;width:177px;height:325px;background:var(--panel-gray);font-family:Arimo,sans-serif}
  .info-heading{position:absolute;left:8px;color:var(--accent-red);font-weight:700;font-size:13px}
  .testimonial{position:absolute;left:8px;top:42px;width:168px;font-size:11px;line-height:13.3px;letter-spacing:.6px;color:var(--ink);white-space:nowrap}
  .testimonial-by{position:absolute;right:24px;top:133px;font-size:11px;letter-spacing:1px;color:var(--ink)}
  .special-band{position:absolute;left:0;top:155px;width:177px;height:44px;background:var(--white)}
  .special-offer{position:absolute;left:8px;top:181px;font-size:11.5px;color:var(--ink)}
  .service-list{position:absolute;left:7px;top:234px;list-style:none;font-size:11.5px;color:var(--ink)}
  .service-list li{line-height:13.5px}
  .service-list li::before{content:"\2605";font-size:9px;margin-right:1px}

  .results{position:absolute;left:0;top:461px;width:503px;height:153px;background:var(--white)}
  .result{position:absolute;top:0;width:118px;height:153px}
  .tag{position:absolute;top:9px;font-family:"Roboto Condensed",sans-serif;font-weight:400;font-size:9px}
  .tag.before{color:var(--accent-red);left:14px}
  .tag.after{color:var(--accent-green);left:73px}
  .shot{position:absolute;top:25px;width:59px;height:94px;border:1.5px solid}
  .shot.before{left:0;border-color:var(--accent-red)}
  .shot.after{left:59px;border-color:var(--accent-green)}
  .caption{position:absolute;top:123px;left:-6px;width:130px;text-align:center;font-family:"Open Sans",sans-serif;font-weight:400;font-size:8.5px;line-height:11px;color:var(--ink)}

  .footer{position:absolute;left:0;top:614px;width:503px;height:105px;background:var(--footer-red);font-family:"Open Sans",sans-serif}
  .partner{position:absolute;left:13px;top:42px;width:100px;height:20px;background:var(--white);color:var(--accent-red);
    font-size:10.5px;font-weight:600;text-align:center;line-height:20px}
  .locations{position:absolute;left:126px;top:10px;width:255px;height:86px;background:var(--locations-red);color:var(--muted);font-size:8.5px;line-height:10px}
  .locations h3{position:absolute;top:7px;width:100%;text-align:center;color:var(--white);font-size:10.5px;font-weight:700}
  .loc{position:absolute;white-space:nowrap}
  .brand{position:absolute;left:392px;top:20px;width:100px;text-align:center;color:var(--brand-blue);font-size:11px;font-weight:600}
  .brand .dot{display:block;margin:0 auto 6px;width:36px;height:36px;border-radius:50%;border:2px solid var(--brand-blue)}
</style>
</head>
<body>
<div class="stage">
  <div class="guide-line" style="left:304px;top:140px;width:3px;height:720px"></div>
  <div class="guide-label" style="left:281px;top:475px;width:50px;height:51px">10<br>INC</div>
  <div class="guide-line" style="left:348px;top:892px;width:504px;height:3px"></div>
  <div class="guide-label" style="left:574px;top:868px;width:51px;height:51px">7<br>INC</div>

  <article class="ad">
    <header class="header">
      <div class="name">M.R. HALDANE’S</div>
      <div class="title">Breast and Body Solutions</div>
    </header>

    <section class="doctor-panel">
      <div class="portrait" role="img" aria-label="Portrait photo of the surgeon in a dark suit"></div>
      <div class="doctor-name">M. R. Haldane, M.D.</div>
      <div class="doctor-cred">Board Certified,<br>Award Winning Plastic Surgeon</div>
      <div class="specialty">Specialist in minimal scarring,<br>natural look techniques using<br>advanced laser technology.</div>
    </section>

    <div class="hero" role="img" aria-label="Photo of a woman in a white shirt and riding trousers walking away against a dark backdrop"></div>

    <aside class="info-panel">
      <div class="info-heading" style="top:13px">Testimonial</div>
      <p class="testimonial">“Dr. Haldane combines<br>artistry, a caring bedside<br>manner, professionalism<br>and safety…. As a medical<br>professional myself and<br>his very satisfied patient,<br>I highly recommend him”.</p>
      <div class="testimonial-by">T.M.</div>
      <div class="special-band"></div>
      <div class="info-heading" style="top:159px">January Special</div>
      <div class="special-offer">Vela Peel ™ $199</div>
      <div class="info-heading" style="top:213px">Non-Surgical Services</div>
      <ul class="service-list">
        <li>Lumitox ™</li>
        <li>Fillara ™</li>
        <li>Dermasse ™</li>
        <li>Laser Treatments</li>
      </ul>
    </aside>

    <section class="results">
      <div class="result" style="left:10px">
        <span class="tag before">BEFORE</span><span class="tag after">AFTER</span>
        <div class="shot before" role="img" aria-label="Before photo of breast enhancement" style="background:radial-gradient(ellipse at 45% 55%,#e8a070,#c07040 60%,#8a4a2a)"></div>
        <div class="shot after" role="img" aria-label="After photo of breast enhancement" style="background:radial-gradient(ellipse at 45% 55%,#eaa474,#c27242 60%,#8c4c2c)"></div>
        <div class="caption">BREAST ENHANCEMENT</div>
      </div>
      <div class="result" style="left:133px">
        <span class="tag before">BEFORE</span><span class="tag after">AFTER</span>
        <div class="shot before" role="img" aria-label="Before photo of laser liposuction on the back" style="background:linear-gradient(90deg,#2e5fb8 0%,#a8845a 14%,#c09a70 50%,#a8845a 86%,#2e5fb8 100%)"></div>
        <div class="shot after" role="img" aria-label="After photo of laser liposuction on the back" style="background:linear-gradient(90deg,#2e5fb8 0%,#e0ccb6 14%,#f0e4d8 50%,#e0ccb6 86%,#2e5fb8 100%)"></div>
        <div class="caption">AWAKE LASER LIPOSUCTION<br>TRIO ™</div>
      </div>
      <div class="result" style="left:257px">
        <span class="tag before">BEFORE</span><span class="tag after">AFTER</span>
        <div class="shot before" role="img" aria-label="Before photo of S lift" style="background:linear-gradient(90deg,#8fa8c4 0%,#b8c4d0 30%,#c8968a 60%,#ececec 100%)"></div>
        <div class="shot after" role="img" aria-label="After photo of S lift" style="background:linear-gradient(90deg,#ece6e0 0%,#d4a28c 45%,#7a4a36 75%,#2a1c16 100%)"></div>
        <div class="caption">S LIFT</div>
      </div>
      <div class="result" style="left:379px">
        <span class="tag before">BEFORE</span><span class="tag after">AFTER</span>
        <div class="shot before" role="img" aria-label="Before photo of tummy tuck" style="background:linear-gradient(90deg,#2e5fb8 0%,#bcb0a8 14%,#d4ccc6 50%,#bcb0a8 86%,#2e5fb8 100%)"></div>
        <div class="shot after" role="img" aria-label="After photo of tummy tuck" style="background:linear-gradient(#c8946c 0%,#d4a078 65%,#5a3c8a 85%,#2e5fb8 100%)"></div>
        <div class="caption">TUMMY TUCK</div>
      </div>
    </section>

    <footer class="footer">
      <div class="partner">Sculptline Trio</div>
      <div class="locations">
        <h3>LOCATIONS</h3>
        <div class="loc" style="left:6px;top:27px">4120 Marlow Ave Suite<br>1200 Ashbury, MD&nbsp; 20900</div>
        <div class="loc" style="left:6px;top:57px">2260 Fenwick Pike Ashgrove,<br>MD&nbsp; 21800</div>
        <div class="loc" style="left:154px;top:27px">Phone<br>(301)555-0192</div>
        <div class="loc" style="left:154px;top:57px">Web<br>www.corvelmd.com</div>
      </div>
      <div class="brand"><span class="dot"></span>Corvel Aesthetics</div>
    </footer>
  </article>
</div>
</body>
</html>
```